Bramwell Resources Ltd. - Refreshed business card challenge

A revised, refreshed business card design for my oil and gas company using my existing logo. Feel free to be as creative as you like!

Target Market(s)

bankers, lawyers

Industry/Entity Type

Oil And Gas Exploration

Contact Information for Business Card

See the "Must Haves" section

Font styles to use
Serif
Sans Serif

Colors

Designer to choose colors to be used in the design.

Requirements
Must have
• Existing business logo, name, title, email, phone number, business address
• Neil Hadley, CA, CPA
• Vice President Finance & Chief Financial Officer
• nhadley@bramwellresources-mail.com
• office: (587)555-0142
• cell: (403)555-0187
• 1400, 815 4 Street S.W.
• Calgary, AB
• T2P 4K8
Should not have
• Should not be plain and boring.

```html
<!DOCTYPE html>
<html lang="en">
<head>
<meta charset="utf-8">
<title>Bramwell Resources Ltd. – Business Card</title>
<link href="https://fonts.googleapis.com/css2?family=Roboto:wght@400;700;900&family=Fira+Sans+Extra+Condensed:wght@600&display=swap" rel="stylesheet">
<style>
  :root {
    --backdrop: #1b1b1c;
    --card: #232324;
    --card-edge: #2e2e30;
    --green: #1f7a4d;
    --green-light: #2f8f5c;
    --brown: #8a4f26;
    --ink: #e9e9e9;
    --silver: #9a9a9c;
  }
  * { margin: 0; padding: 0; box-sizing: border-box; }
  html, body {
    width: 1200px; height: 900px; overflow: hidden;
    background: var(--backdrop);
    font-family: "Roboto", Arial, sans-serif;
  }
  .canvas {
    position: relative; width: 1200px; height: 900px;
  }
  .card {
    position: absolute; left: 250px; width: 700px; height: 400px;
    background: var(--card);
    border: 1px solid var(--card-edge);
    overflow: hidden;
  }
  .card--front { top: 40px; }
  .card--back { top: 465px; }

  /* front */
  .front-logo {
    position: absolute; left: 0; right: 0; top: 168px;
    display: flex; align-items: center; justify-content: center; gap: 16px;
  }
  .front-logo__mark {
    width: 22px; height: 22px; background: var(--silver);
  }
  .front-logo__name {
    font-weight: 900; font-size: 46px; color: var(--silver); letter-spacing: -0.5px;
  }

  /* back */
  .back-logo {
    position: absolute; left: 40px; top: 34px;
    font-weight: 900; font-size: 46px; color: var(--green); letter-spacing: -0.5px;
  }
  .person { position: absolute; left: 42px; top: 128px; }
  .person__name {
    font-family: "Fira Sans Extra Condensed", "Arial Narrow", sans-serif;
    font-weight: 600; font-size: 28px; color: var(--green-light);
  }
  .person__title {
    margin-top: 6px; font-size: 16px; line-height: 20px; color: var(--ink);
  }
  .contacts {
    position: absolute; left: 42px; top: 252px;
    display: grid; grid-template-columns: 160px auto; row-gap: 8px; column-gap: 18px;
    font-size: 15px; color: var(--ink);
  }
  .contact { display: flex; align-items: center; gap: 9px; white-space: nowrap; }
  .contact--wide { grid-column: 1 / 3; }
  .contact svg { width: 15px; height: 15px; fill: var(--green-light); flex: none; }

  .forest-art {
    position: absolute; left: 505px; top: 100px; width: 170px; height: 265px;
    background: linear-gradient(180deg, #2a8a58 0%, #1f7a4d 70%, #6b4424 100%);
    border-radius: 85px 85px 6px 6px;
  }
  .ground { position: absolute; left: 0; bottom: 0; width: 700px; height: 60px; }
</style>
</head>
<body>
<main class="canvas">

  <section class="card card--front" aria-label="Card front">
    <div class="front-logo">
      <span class="front-logo__mark"></span>
      <span class="front-logo__name">Bramwell Resources</span>
    </div>
  </section>

  <section class="card card--back" aria-label="Card back">
    <div class="back-logo">Bramwell Resources</div>

    <div class="person">
      <p class="person__name">Neil Hadley, CA, CPA</p>
      <p class="person__title">Vice President Finance &amp;<br>Chief Financial Officer</p>
    </div>

    <div class="contacts">
      <div class="contact">
        <svg viewBox="0 0 24 24"><path d="M6.6 10.8a15 15 0 0 0 6.6 6.6l2.2-2.2c.3-.3.7-.4 1-.2 1.1.4 2.3.6 3.6.6.6 0 1 .4 1 1V20c0 .6-.4 1-1 1A17 17 0 0 1 3 4c0-.6.4-1 1-1h3.5c.6 0 1 .4 1 1 0 1.3.2 2.5.6 3.6.1.3 0 .7-.2 1z"/></svg>
        (587)555-0142
      </div>
      <div class="contact">
        <svg viewBox="0 0 24 24"><path d="M2 4l10 7 10-7v-.5H2zM2 6.5V20h20V6.5l-10 7z"/></svg>
        nhadley@bramwellresources-mail.com
      </div>
      <div class="contact">
        <svg viewBox="0 0 24 24"><path d="M7 1h10a2 2 0 0 1 2 2v18a2 2 0 0 1-2 2H7a2 2 0 0 1-2-2V3a2 2 0 0 1 2-2zm0 3v14h10V4zm5 15.5a1.2 1.2 0 1 0 0 2.4 1.2 1.2 0 0 0 0-2.4z"/></svg>
        (403)555-0187
      </div>
      <div class="contact">
        <svg viewBox="0 0 24 24"><path d="M12 2a10 10 0 1 0 0 20 10 10 0 0 0 0-20zm6.9 6h-3a15 15 0 0 0-1.3-3.9A8 8 0 0 1 18.9 8zM12 4c.8 1.2 1.5 2.5 1.9 4h-3.8c.4-1.5 1.1-2.8 1.9-4zM4.3 14a8 8 0 0 1 0-4h3.4a16 16 0 0 0 0 4zm.8 2h3a15 15 0 0 0 1.3 3.9A8 8 0 0 1 5.1 16zm3-8h-3a8 8 0 0 1 4.3-3.9C8.8 5.3 8.4 6.6 8.1 8zM12 20c-.8-1.2-1.5-2.5-1.9-4h3.8c-.4 1.5-1.1 2.8-1.9 4zm2.3-6H9.7a14 14 0 0 1 0-4h4.6a14 14 0 0 1 0 4zm.3 5.9c.6-1.2 1-2.5 1.3-3.9h3a8 8 0 0 1-4.3 3.9zm1.7-5.9a16 16 0 0 0 0-4h3.4a8 8 0 0 1 0 4z"/></svg>
        www.bramwellresources-mail.com
      </div>
      <div class="contact contact--wide">
        <svg viewBox="0 0 24 24"><path d="M12 2a7 7 0 0 0-7 7c0 5 7 13 7 13s7-8 7-13a7 7 0 0 0-7-7zm0 9.5a2.5 2.5 0 1 1 0-5 2.5 2.5 0 0 1 0 5z"/></svg>
        1400, 815 4 Street S.W. Calgary, AB T2P 4K8
      </div>
    </div>

    <div class="forest-art" role="img" aria-label="Illustration of a tall green conifer tree with smaller trees at its base"></div>

    <svg class="ground" viewBox="0 0 700 60" preserveAspectRatio="none" aria-hidden="true">
      <path d="M0 44 H470 Q560 44 600 30 Q650 18 700 26 V60 H0 Z" fill="var(--brown)"/>
    </svg>
  </section>

</main>
</body>
</html>
```